Stunning Podcast Cover Design for The Morning Harbor Hour!!

I need a design for my new podcast.
I will need it in a variety of size/formats, such as a large version for my podcast website homepage, the thumbnail for Tunewell, Pondcast, Vexa Stream and more.

The podcast is called "The Morning Harbor Hour" and it includes topics such as: business, entrepreneurship, finance, budgeting, estate planning, end-of-life planning, travel, business and personal stories featuring people from all over the world, life in general, and more.

I don't have a vision in mind so am looking for creativity but it definitely needs to have the colour gold in it somewhere! No cartoon characters please.

I will provide comments/feedback to each designer.

***UPDATE: Please see some photos of me that can be used in the podcast design.

Here is some tips on creating podcast designs. https://www.castleafy.example/blog/10-tips-create-awesome-podcast-artwork

Target Market(s)

Adults 25 - 65

Font styles to use
Other font styles liked:
• something modern - see my company logo as an example

Colors

Designer to choose colors to be used in the design.

Requirements
Must have
• The colour gold in it
Nice to have
• I feel like the word "The" should be smaller then the other three words.
• I would like to see designs with a white coloured background and a black coloured one also...
• Perhaps designs with a filter over the photo, and without.
• Perhaps use my photo, or don't use my photo!
• Please see some photos of me that can be used in the podcast design.
• Here is some tips on creating podcast designs. https://www.castleafy.example/blog/10-tips-create-awesome-podcast-artwork
Should not have
• cartoon characters
• Corny 1990's "Evenings Among the Gilded and Glamorous" look - see https://www.vidorama.example/watch?v=Q7T2KX8PLBZ

```html
<!DOCTYPE html>
<html lang="en">
<head>
<meta charset="utf-8">
<title>The Morning Harbor Hour – Podcast Cover</title>
<link rel="stylesheet" href="https://fonts.googleapis.com/css2?family=Josefin+Sans:wght@300;700&display=swap">
<style>
  :root {
    --wall-warm: #cdbb84;
    --wall-light: #d9dcd4;
    --vignette: rgba(31, 58, 52, 0.75);
    --gold: #f0d98a;
    --gold-deep: #b8903a;
    --glow: rgba(255, 236, 170, 0.75);
    --photo-top: #4a3a30;
    --photo-bottom: #2b2623;
    --brand-ink: #17181a;
  }
  html, body {
    margin: 0;
    padding: 0;
    width: 1200px;
    height: 1200px;
    overflow: hidden;
    background: #ffffff;
  }
  .cover {
    position: relative;
    width: 1200px;
    height: 1200px;
    overflow: hidden;
    font-family: "Josefin Sans", "Futura", sans-serif;
  }
  .backdrop {
    position: absolute;
    inset: 0;
    background:
      radial-gradient(ellipse 75% 65% at 35% 30%, rgba(255, 240, 190, 0.55), rgba(0,0,0,0) 70%),
      linear-gradient(160deg, var(--wall-warm) 0%, var(--wall-warm) 52%, var(--wall-light) 62%, #b9c4bd 100%);
  }
  .backdrop::after {
    content: "";
    position: absolute;
    inset: 0;
    background: radial-gradient(ellipse 85% 85% at 40% 45%, rgba(0,0,0,0) 55%, var(--vignette) 100%);
  }
  .host-photo {
    position: absolute;
    left: 700px;
    top: 196px;
    width: 500px;
    height: 1004px;
    background: linear-gradient(180deg, var(--photo-top) 0%, var(--photo-bottom) 100%);
  }
  .title {
    position: absolute;
    left: 62px;
    top: 50px;
    margin: 0;
    font-weight: 700;
    text-transform: uppercase;
    line-height: 1;
    color: var(--gold);
    text-shadow:
      0 0 18px var(--glow),
      3px 4px 0 var(--gold-deep),
      5px 8px 14px rgba(60, 40, 10, 0.45);
  }
  .title span { display: block; }
  .title .word-the {
    font-size: 64px;
    letter-spacing: 2px;
    margin-bottom: 24px;
  }
  .title .word-main {
    font-size: 108px;
    letter-spacing: 1px;
    margin-bottom: 30px;
  }
  .title .word-last {
    font-size: 90px;
    margin-left: 250px;
    letter-spacing: 2px;
  }
  .brand {
    position: absolute;
    left: 72px;
    top: 1018px;
    display: flex;
    align-items: center;
    gap: 18px;
    color: var(--brand-ink);
    font-weight: 300;
    font-size: 58px;
    letter-spacing: 10px;
  }
  .brand-square {
    width: 22px;
    height: 22px;
    border: 2px solid var(--brand-ink);
  }
</style>
</head>
<body>
  <div class="cover">
    <div class="backdrop" role="img" aria-label="Photograph of a painted brick wall, warm gold upper half and pale grey lower half"></div>
    <div class="host-photo" role="img" aria-label="Photograph of the podcast host smiling, wearing glasses, a dark top and a faux fur vest"></div>
    <h1 class="title">
      <span class="word-the">The</span>
      <span class="word-main">Morning</span>
      <span class="word-main">Harbor</span>
      <span class="word-last">Hour</span>
    </h1>
    <div class="brand">
      <span class="brand-square"></span>
      <span class="brand-name">VELDANE</span>
    </div>
  </div>
</body>
</html>
```